Business Card Design for Varnel

I've already got the logo, but I'd like to see some interesting designs.

I don't want anything to complex. I like it simple,yet innovative, like the logo.

My business is System Administration for small to medium size businesses, so that will be my main target audience.
Updates

hey all, the png has been uploaded.

Hey all,

If you are submitting the back side of the card, I'd like the top bit of the card to be Varnel Solutions and the logo, the bottom of the card the website, with a white background.

The middle I'd like to leave blank for a quote that will be printed on each card.

Thanks!

Doug

Industry/Entity Type

Business

```html
<!DOCTYPE html>
<html lang="en">
<head>
<meta charset="utf-8">
<title>Varnel Solutions – Business Card</title>
<link rel="stylesheet" href="https://fonts.googleapis.com/css2?family=Arimo:wght@400;700&display=swap">
<style>
  :root {
    --brand-blue: #2776b0;
    --ink-dark: #1c1c1c;
    --ink-body: #333333;
    --card-white: #ffffff;
    --page-bg: #e9e4dc;
  }
  * { box-sizing: border-box; margin: 0; padding: 0; }
  html, body {
    width: 1200px; height: 900px; overflow: hidden;
    background: var(--page-bg);
    font-family: "Arimo", Arial, sans-serif;
  }
  .canvas { position: relative; width: 1200px; height: 900px; }

  .card {
    position: absolute;
    width: 560px; height: 320px;
    background: var(--card-white);
    box-shadow: 0 4px 14px rgba(0,0,0,0.18);
    overflow: hidden;
  }
  .card--front { left: 70px; top: 110px; }
  .card--back  { left: 570px; top: 470px; }

  .card__shapes { position: absolute; inset: 0; }

  .brand {
    position: absolute;
    display: flex; align-items: center; gap: 12px;
    font-weight: 700; font-size: 30px; letter-spacing: -0.5px;
  }
  .brand__dot { width: 46px; height: 46px; border-radius: 50%; flex: none; }
  .card--front .brand { left: 38px; top: 100px; color: var(--brand-blue); }
  .card--front .brand__dot { background: var(--brand-blue); }

  .holder { position: absolute; left: 345px; top: 72px; }
  .holder__name { font-size: 19px; font-weight: 700; color: var(--ink-dark); }
  .holder__role { font-size: 14px; color: var(--brand-blue); margin-top: 2px; }

  .contacts { position: absolute; left: 330px; top: 128px; list-style: none; }
  .contacts li {
    display: flex; align-items: center; gap: 8px;
    font-size: 13px; color: var(--brand-blue); line-height: 17px;
  }
  .contacts svg { width: 14px; height: 14px; fill: var(--brand-blue); flex: none; }

  .address {
    position: absolute; left: 38px; top: 205px;
    font-size: 13px; line-height: 17px; color: var(--ink-body);
  }

  .card--back .brand { left: 0; right: 0; top: 70px; justify-content: center; color: var(--card-white); }
  .card--back .brand__dot { background: var(--card-white); }

  .website {
    position: absolute; left: 0; right: 0; top: 268px;
    text-align: center; font-size: 17px; color: var(--brand-blue);
  }
</style>
</head>
<body>
<main class="canvas">

  <section class="card card--front" aria-label="Business card front">
    <svg class="card__shapes" width="560" height="320" viewBox="0 0 560 320" aria-hidden="true">
      <rect x="0" y="0" width="560" height="8" fill="var(--brand-blue)"/>
      <path d="M0,258 L232,258 L262,250 L560,182 L560,320 L0,320 Z" fill="var(--brand-blue)"/>
    </svg>

    <div class="brand"><span class="brand__dot"></span>Varnel Solutions</div>

    <div class="holder">
      <p class="holder__name">Your Name</p>
      <p class="holder__role">Your position......</p>
    </div>

    <ul class="contacts">
      <li>
        <svg viewBox="0 0 24 24"><path d="M6.6 10.8a15 15 0 0 0 6.6 6.6l2.2-2.2a1 1 0 0 1 1-.25 11.4 11.4 0 0 0 3.6.57 1 1 0 0 1 1 1V20a1 1 0 0 1-1 1A17 17 0 0 1 3 4a1 1 0 0 1 1-1h3.5a1 1 0 0 1 1 1c0 1.25.2 2.45.57 3.57a1 1 0 0 1-.25 1z"/></svg>
        Yr Tell: Number
      </li>
      <li>
        <svg viewBox="0 0 24 24"><path d="M7 1h10a2 2 0 0 1 2 2v18a2 2 0 0 1-2 2H7a2 2 0 0 1-2-2V3a2 2 0 0 1 2-2zm0 3v13h10V4zm5 15a1 1 0 1 0 0 2 1 1 0 0 0 0-2z"/></svg>
        Yr Mobile 4n Number
      </li>
      <li>
        <svg viewBox="0 0 24 24"><path d="M2 5h20v14H2zm2 2v.5l8 5 8-5V7zm0 2.8V17h16V9.8l-8 5z"/></svg>
        Yr e mail
      </li>
    </ul>

    <p class="address">Your Address:xxxxxxxxxx,<br>xxxxxxxxxx,xxxxxxxx.</p>
  </section>

  <section class="card card--back" aria-label="Business card back">
    <svg class="card__shapes" width="560" height="320" viewBox="0 0 560 320" aria-hidden="true">
      <rect x="0" y="6" width="560" height="234" fill="var(--brand-blue)"/>
    </svg>

    <div class="brand"><span class="brand__dot"></span>Varnel Solutions</div>

    <p class="website">www.Your Web Site.com</p>
  </section>

</main>
</body>
</html>
```